Business Card design for shipping company 'FARNHOLT MARITIME LTD'

Classic / traditional business card in black Garamond / Times New Roman or similar text for a shipping / marine transport company, containing the following information:

QUOTE

FARNHOLT MARITIME LTD

PETER CALLOWAY FICS

T: +44 7923 615087
E: vessels@farnholt-mar.com

UNQUOTE

Target Market(s)

Marine / Shipping industry

Contact Information for Business Card

FARNHOLT MARITIME LTD PETER CALLOWAY FICS T: +44 7923 615087 E: vessels@farnholt-mar.com

Font styles to use
Serif

Colors

Designer to choose colors to be used in the design.

Requirements
Must have
• Garamond / Times New Roman or similar text in black colour

```html
<!DOCTYPE html>
<html lang="en">
<head>
<meta charset="utf-8">
<title>Farnholt Maritime Ltd – Business Card</title>
<link rel="stylesheet" href="https://fonts.googleapis.com/css2?family=Tinos:wght@400;700&display=swap">
<style>
  :root {
    --navy: #1b1e54;
    --ink: #262626;
    --paper: #ffffff;
    --backdrop: #d6d5d1;
    --rule: #555555;
  }
  * { box-sizing: border-box; margin: 0; padding: 0; }
  html, body {
    width: 1200px;
    height: 1056px;
    overflow: hidden;
    background: var(--backdrop);
    font-family: "Tinos", "Times New Roman", serif;
    color: var(--ink);
  }
  .canvas {
    position: relative;
    width: 1200px;
    height: 1056px;
  }
  .card {
    position: absolute;
    left: 230px;
    width: 740px;
    height: 422px;
    background: var(--paper);
    box-shadow: 0 10px 24px rgba(0,0,0,0.22);
    overflow: hidden;
  }
  .card--front { top: 70px; }
  .card--back  { top: 560px; }

  .card__band {
    position: absolute;
    left: 0;
    top: 30px;
    width: 100%;
    height: 78px;
    background: var(--navy);
    display: flex;
    align-items: center;
    padding-left: 34px;
  }
  .card__band-name {
    color: var(--paper);
    font-weight: 700;
    font-size: 32px;
    letter-spacing: 0.5px;
  }
  .card__base {
    position: absolute;
    left: 0;
    bottom: 0;
    width: 100%;
    height: 26px;
    background: var(--navy);
  }

  .person {
    position: absolute;
    left: 150px;
    top: 172px;
  }
  .person__name {
    font-weight: 700;
    font-size: 46px;
    letter-spacing: 0.5px;
    color: var(--ink);
    white-space: nowrap;
  }
  .person__rule {
    display: block;
    margin: 6px 0 0 110px;
    width: 400px;
    height: 4px;
  }
  .contact {
    margin: 14px 0 0 236px;
    font-size: 26px;
    line-height: 1.25;
    color: var(--ink);
  }

  .back {
    position: absolute;
    left: 0;
    top: 0;
    width: 100%;
    height: 396px;
    display: flex;
    flex-direction: column;
    align-items: center;
    justify-content: center;
    gap: 54px;
  }
  .back__name {
    font-weight: 700;
    font-size: 46px;
    letter-spacing: 0.5px;
    color: var(--ink);
    white-space: nowrap;
  }
  .back__email {
    font-size: 24px;
    letter-spacing: 11px;
    color: var(--ink);
  }
</style>
</head>
<body>
<main class="canvas">
  <section class="card card--front" aria-label="Business card front">
    <div class="card__band">
      <span class="card__band-name">FARNHOLT MARITIME LTD</span>
    </div>
    <div class="person">
      <h1 class="person__name">PETER CALLOWAY FICS</h1>
      <svg class="person__rule" viewBox="0 0 400 4" preserveAspectRatio="none" aria-hidden="true">
        <defs>
          <linearGradient id="ruleFade" x1="0" x2="1">
            <stop offset="0" stop-color="#555" stop-opacity="0.15"/>
            <stop offset="0.5" stop-color="#333" stop-opacity="1"/>
            <stop offset="1" stop-color="#555" stop-opacity="0.15"/>
          </linearGradient>
        </defs>
        <rect x="0" y="1" width="400" height="2" fill="url(#ruleFade)"/>
      </svg>
      <p class="contact">T : +44 7923 615087<br>E : vessels@farnholt-mar.com</p>
    </div>
    <div class="card__base"></div>
  </section>

  <section class="card card--back" aria-label="Business card back">
    <div class="back">
      <h2 class="back__name">FARNHOLT MARITIME LTD</h2>
      <p class="back__email">vessels@farnholt-mar.com</p>
    </div>
    <div class="card__base"></div>
  </section>
</main>
</body>
</html>
```